Brava Nest (Smart Home, Installation, Repair Industry) (Contest)

Looking for a website design for my company
Services we offer:
Phone Repair
TV Mounting
Security Camera Installation
Networking / Wi-Fi
Smart Home Services
IT Support

Looking for a website similar to trovely.example

Few tabs
About Us
Contact Us
Areas Served
Pricing and Services

```html
<!DOCTYPE html>
<html lang="en">
<head>
<meta charset="utf-8">
<title>Brava Nest — Smart Home Maintenance</title>
<link href="https://fonts.googleapis.com/css2?family=Montserrat:wght@700;800&family=Mulish:wght@400;600;700&family=Roboto+Condensed:wght@300&display=swap" rel="stylesheet">
<style>
:root{
  --orange:#f7931e;
  --orange-soft:#fbb25c;
  --ink:#111111;
  --night:#1c1c1c;
  --slate:#4a4a4a;
  --mist:#f1f1f1;
  --text:#8a8a8a;
  --white:#ffffff;
}
*{margin:0;padding:0;box-sizing:border-box}
html,body{width:1200px;height:3323px;overflow:hidden;background:var(--white)}
body{position:relative;font-family:"Mulish",sans-serif;color:var(--text)}
.abs{position:absolute}
.heading{font-family:"Montserrat",sans-serif;font-weight:800;color:var(--ink)}
.btn{position:absolute;display:flex;align-items:center;justify-content:center;background:var(--orange);color:var(--white);border-radius:30px;font-size:16px;font-weight:600;text-transform:uppercase}
.photo{position:absolute;border-radius:10px}

/* header */
.nav{left:77px;top:31px;width:1046px;height:72px;background:var(--white);border-radius:3px;box-shadow:0 4px 14px rgba(0,0,0,.12);display:flex;align-items:center}
.brand{font-family:"Mulish",sans-serif;font-weight:700;font-size:42px;color:var(--orange);margin-left:22px;letter-spacing:-.5px}
.menu{display:flex;gap:38px;margin-left:auto;margin-right:22px;font-size:16px;color:#555;align-items:center;height:100%}
.menu span{position:relative;height:100%;display:flex;align-items:center}
.menu .active{color:var(--orange);font-weight:600}
.menu .active::after{content:"";position:absolute;left:0;right:0;bottom:0;height:3px;background:var(--orange)}

/* hero */
.hero-title{left:79px;top:204px;font-size:41px;line-height:54px;color:var(--white)}
.hero-title em{font-style:normal;color:var(--orange)}
.hero-copy{left:79px;top:328px;width:590px;font-size:16.5px;line-height:29px;color:#eee}
.arrow{position:absolute;top:520px;width:47px;height:47px;border-radius:50%;background:#f3f3f3;display:flex;align-items:center;justify-content:center}

/* cards */
.card{position:absolute;top:895px;width:313px;height:365px;border-radius:8px;overflow:hidden}
.card .shade{position:absolute;inset:0;background:linear-gradient(180deg,rgba(0,0,0,.15),rgba(0,0,0,.7))}
.card .badge{position:absolute;left:30px;top:105px}
.card h3{position:absolute;left:33px;top:212px;font-family:"Mulish",sans-serif;font-weight:600;font-size:21px;color:var(--white)}
.card p{position:absolute;left:33px;top:252px;width:250px;font-size:15px;line-height:23px;color:#eee}

/* tiles */
.tile{position:absolute;width:188px;height:188px;border-radius:10px;padding:22px}
.tile span{position:absolute;left:22px;bottom:30px;font-size:18px;font-weight:600}

.partner{position:absolute;top:2719px;width:193px;height:78px;border:2px solid #eeeeee;border-radius:4px;display:flex;align-items:center;justify-content:center}
.partner i{display:block;width:120px;height:22px;border-radius:4px;background:#dedede}

.foot-link{position:absolute;font-size:15px;color:var(--white)}
</style>
</head>
<body>

<!-- hero backdrop -->
<svg class="abs" style="left:0;top:0" width="1200" height="700" viewBox="0 0 1200 700" role="img" aria-label="Dimly lit modern living room interior">
  <defs>
    <linearGradient id="room" x1="0" y1="0" x2="1" y2="1">
      <stop offset="0" stop-color="#3a3a3a"/><stop offset=".5" stop-color="#262626"/><stop offset="1" stop-color="#141414"/>
    </linearGradient>
  </defs>
  <path d="M0,0 H1085 C1112,40 1112,110 1080,150 C1020,230 960,300 880,420 C800,560 720,680 580,678 C430,676 380,560 250,480 C150,420 60,410 0,410 Z" fill="url(#room)"/>
</svg>
<div class="photo" role="img" aria-label="Smart security camera and phone dashboard app" style="left:790px;top:205px;width:320px;height:470px;border-radius:40px;background:radial-gradient(circle at 40% 35%,#ffffff,#e4e4e4 55%,rgba(210,210,210,.6) 78%,rgba(0,0,0,0) 100%)"></div>
<div class="photo" role="img" aria-label="Wireless door sensor" style="left:605px;top:495px;width:200px;height:120px;border-radius:50px;background:radial-gradient(circle at 45% 40%,#ffffff,#e2e2e2 60%,rgba(0,0,0,0) 100%)"></div>

<header class="abs nav">
  <div class="brand">Brava Nest</div>
  <nav class="menu">
    <span class="active">Home</span><span>About Us</span><span>Area Served</span><span>Pricing &amp; srvices</span><span>Contact Us</span>
    <svg width="22" height="22" viewBox="0 0 22 22"><circle cx="9" cy="9" r="7" fill="none" stroke="#f7931e" stroke-width="2"/><path d="M14 14l6 6" stroke="#f7931e" stroke-width="2"/></svg>
  </nav>
</header>

<h1 class="abs heading hero-title"><em>Smart</em> Home <em>Maintenance</em><br>Made <em>Easy</em></h1>
<p class="abs hero-copy">Lorem ipsum dolor sit amet, consectetur adipiscing elit, sed do eiusmod tempor incididunt ut labore et dolore magna aliqua.</p>
<div class="btn" style="left:77px;top:417px;width:166px;height:51px">Check it now</div>
<div class="arrow" style="left:78px"><svg width="12" height="16"><path d="M9 2L3 8l6 6" fill="none" stroke="#f7931e" stroke-width="2"/></svg></div>
<div class="arrow" style="left:133px"><svg width="12" height="16"><path d="M3 2l6 6-6 6" fill="none" stroke="#222" stroke-width="2"/></svg></div>

<!-- what we do -->
<svg class="abs" style="left:0;top:664px" width="130" height="190" viewBox="0 0 130 190"><path d="M0,20 C20,5 45,-5 55,15 C65,40 70,55 95,70 C125,90 110,150 75,160 C40,170 30,190 0,188 Z" fill="#f7931e"/></svg>
<h2 class="abs heading" style="left:79px;top:748px;font-size:35px">What We Do</h2>
<p class="abs" style="left:79px;top:808px;width:620px;font-size:15.5px;line-height:26px">Lorem ipsum dolor sit amet, consectetur adipiscing elit, sed do eiusmod tempor incididunt ut labore et dolore magna aliqua.</p>

<div class="card" style="left:77px">
  <div class="abs" role="img" aria-label="Technician mounting a television on a living room wall" style="inset:0;background:linear-gradient(135deg,#6d6d6d,#3b3b3b 60%,#2a2a2a)"></div>
  <div class="shade"></div>
  <svg class="badge" width="96" height="84" viewBox="0 0 96 84"><path d="M10,8 C40,-4 80,0 92,20 C100,40 88,70 60,80 C30,90 4,72 2,44 C0,28 2,12 10,8Z" fill="#f7931e"/><rect x="22" y="24" width="36" height="24" rx="2" fill="none" stroke="#fff" stroke-width="2"/><path d="M34 56h12M40 48v8" stroke="#fff" stroke-width="2"/><rect x="60" y="32" width="14" height="26" rx="2" fill="none" stroke="#fff" stroke-width="2"/></svg>
  <h3>TV Mounting</h3>
  <p>Lorem ipsum dolor sconsectetur tempor incididunt ut labore et dolore magna aliqua.</p>
</div>
<div class="card" style="left:444px">
  <div class="abs" role="img" aria-label="Hand holding a phone with a network graphic overlay" style="inset:0;background:linear-gradient(135deg,#2e3440,#1c2430 60%,#2b3f5a)"></div>
  <div class="shade"></div>
  <svg class="badge" width="96" height="84" viewBox="0 0 96 84"><path d="M10,8 C40,-4 80,0 92,20 C100,40 88,70 60,80 C30,90 4,72 2,44 C0,28 2,12 10,8Z" fill="#f7931e"/><rect x="36" y="16" width="20" height="24" rx="3" fill="none" stroke="#fff" stroke-width="2"/><rect x="26" y="44" width="40" height="12" rx="2" fill="none" stroke="#fff" stroke-width="2"/><path d="M32 56v8M46 56v8M60 56v8" stroke="#fff" stroke-width="2"/></svg>
  <h3>Networking / Wi-Fi</h3>
  <p>Lorem ipsum dolor sconsectetur tempor incididunt ut labore et dolore magna aliqua.</p>
</div>
<div class="card" style="left:810px">
  <div class="abs" role="img" aria-label="Technician repairing a phone circuit board" style="inset:0;background:linear-gradient(135deg,#5a5f66,#34383e 60%,#24272b)"></div>
  <div class="shade"></div>
  <svg class="badge" width="96" height="84" viewBox="0 0 96 84"><path d="M10,8 C40,-4 80,0 92,20 C100,40 88,70 60,80 C30,90 4,72 2,44 C0,28 2,12 10,8Z" fill="#f7931e"/><rect x="34" y="14" width="26" height="50" rx="4" fill="none" stroke="#fff" stroke-width="2"/><circle cx="47" cy="36" r="7" fill="none" stroke="#fff" stroke-width="2"/><path d="M43 58h8" stroke="#fff" stroke-width="2"/></svg>
  <h3>Phone Repair</h3>
  <p>Lorem ipsum dolor sconsectetur tempor incididunt ut labore et dolore magna aliqua.</p>
</div>

<div class="btn" style="left:495px;top:1312px;width:208px;height:52px">View all services</div>
<svg class="abs" style="left:1145px;top:1300px" width="55" height="166" viewBox="0 0 55 166"><path d="M55,0 C30,30 0,70 5,110 C10,140 35,150 55,166 Z" fill="#f7931e"/></svg>

<!-- welcome -->
<svg class="abs" style="left:30px;top:1436px" width="505" height="508" viewBox="0 0 505 508"><path d="M200,30 C300,-10 460,-10 500,80 C530,160 430,260 400,340 C360,440 330,510 240,505 C150,500 80,400 30,300 C-20,200 -10,100 60,70 C110,50 150,50 200,30Z" fill="#f7931e"/></svg>
<div class="photo" role="img" aria-label="Mother and daughter relaxing on a living room floor" style="left:77px;top:1480px;width:364px;height:238px;background:linear-gradient(135deg,#eceae6,#c9c4bc 60%,#a9a39a)"></div>
<div class="photo" role="img" aria-label="Hand holding a phone with smart home control icons" style="left:213px;top:1655px;width:364px;height:241px;background:linear-gradient(135deg,#9a8e80,#6d6a67 55%,#4c5a6e);box-shadow:0 6px 20px rgba(0,0,0,.2)"></div>
<h2 class="abs heading" style="left:655px;top:1528px;font-size:35px">Welcome To Brava Nest</h2>
<p class="abs" style="left:656px;top:1589px;width:463px;font-size:15.5px;line-height:26px">Lorem ipsum dolor sit amet, consectetur adipiscing elit, sed do eiusmod tempor incididunt ut labore et dolore magna aliqua. Ut enim ad minim veniam, quis nostrud exercitation ullamco laboris nisi ut aliquip ex ea commodo consequat.</p>
<p class="abs" style="left:656px;top:1709px;width:463px;font-size:15.5px;line-height:26px">Lorem ipsum dolor sit amet, consectetur adipiscing elit, sed do eiusmod tempor incididunt ut labore.</p>
<div class="btn" style="left:654px;top:1792px;width:166px;height:51px">Learn more</div>

<!-- get started -->
<div class="abs" style="left:0;top:2073px;width:1200px;height:312px;background:var(--ink)"></div>
<h2 class="abs heading" style="left:79px;top:2143px;font-size:36px;color:var(--white)">Ready To Get Started...?</h2>
<p class="abs" style="left:79px;top:2203px;width:590px;font-size:16.5px;line-height:29px;color:#eee">Lorem ipsum dolor sit amet, consectetur adipiscing elit, sed do eiusmod tempor incididunt ut labore et dolore magna aliqua.</p>
<svg class="abs" style="left:77px;top:2280px" width="64" height="50" viewBox="0 0 64 50"><rect x="20" y="2" width="24" height="46" rx="4" fill="none" stroke="#f7931e" stroke-width="2.5"/><path d="M28 42h8" stroke="#f7931e" stroke-width="2.5"/><path d="M12 14c-4 6-4 16 0 22M5 9c-7 10-7 22 0 32M52 14c4 6 4 16 0 22M59 9c7 10 7 22 0 32" fill="none" stroke="#f7931e" stroke-width="2.5"/></svg>
<div class="abs" style="left:162px;top:2278px;font-family:'Roboto Condensed',sans-serif;font-weight:300;font-size:42px;color:var(--orange)">123.456.7890</div>

<div class="tile" style="left:935px;top:2021px;background:var(--mist)">
  <svg width="80" height="80" viewBox="0 0 80 80"><rect x="14" y="40" width="50" height="30" rx="3" fill="none" stroke="#222" stroke-width="2.5"/><path d="M30 40v-8h18v8M14 52h50" stroke="#222" stroke-width="2.5" fill="none"/><path d="M20 10l12 12M26 6l-12 12" stroke="#222" stroke-width="2.5"/></svg>
  <span style="color:#222">Installation</span>
</div>
<div class="tile" style="left:707px;top:2147px;background:var(--orange)">
  <svg width="80" height="80" viewBox="0 0 80 80"><path d="M6 34L40 8l34 26" fill="none" stroke="#fff" stroke-width="2.5"/><rect x="14" y="32" width="52" height="40" fill="none" stroke="#fff" stroke-width="2.5"/><rect x="22" y="44" width="14" height="18" fill="none" stroke="#fff" stroke-width="2"/><circle cx="52" cy="50" r="6" fill="none" stroke="#fff" stroke-width="2"/></svg>
  <span style="color:#fff">Smart Home</span>
</div>
<div class="tile" style="left:935px;top:2251px;background:var(--slate)">
  <svg width="80" height="80" viewBox="0 0 80 80"><path d="M12 68l34-34M20 12a12 12 0 0 0 16 16l30 30a6 6 0 0 1-8 8L28 36a12 12 0 0 1-16-16l8 8 8-8z" fill="none" stroke="#f7931e" stroke-width="2.5"/><path d="M60 10l8 8-22 22-8-8z" fill="none" stroke="#f7931e" stroke-width="2.5"/></svg>
  <span style="color:var(--orange)">Repair Industry</span>
</div>

<!-- pricing -->
<h2 class="abs heading" style="left:0;width:1200px;text-align:center;top:2456px;font-size:35px">Pricing &amp; Services</h2>
<p class="abs" style="left:300px;width:600px;text-align:center;top:2516px;font-size:15.5px;line-height:26px">Lorem ipsum dolor sit amet, consectetur adipiscing elit, sed do eiusmod tempor incididunt&nbsp; reprehenderit in voluptate velit esse cillum.</p>
<div class="btn" style="left:517px;top:2594px;width:167px;height:52px">Get pricing</div>

<div class="partner" style="left:77px"><i></i></div>
<div class="partner" style="left:290px"><i></i></div>
<div class="partner" style="left:503px"><i></i></div>
<div class="partner" style="left:717px"><i></i></div>
<div class="partner" style="left:930px"><i></i></div>
<svg class="abs" style="left:568px;top:2823px" width="64" height="18"><circle cx="10" cy="9" r="6.5" fill="none" stroke="#bbb" stroke-width="1.5"/><circle cx="31" cy="9" r="7" fill="#999"/><circle cx="52" cy="9" r="6.5" fill="none" stroke="#bbb" stroke-width="1.5"/></svg>

<!-- footer -->
<svg class="abs" style="left:0;top:2905px" width="1200" height="418" viewBox="0 0 1200 418">
  <path d="M0,30 C40,40 120,45 160,40 C300,10 480,-5 620,10 C720,20 800,60 860,40 C960,5 1080,20 1200,60 V418 H0Z" fill="#f7931e"/>
  <path d="M0,30 C60,30 120,35 160,40 C100,60 40,70 0,80Z" fill="#111"/>
  <path d="M740,70 C820,40 920,0 1010,5 C1100,10 1160,50 1200,85 V150 C1150,148 1060,145 960,145 C870,140 800,105 740,70Z" fill="#111"/>
</svg>
<div class="abs" style="left:79px;top:3030px;font-weight:700;font-size:40px;color:var(--white);letter-spacing:-.5px">Brava Nest</div>
<p class="abs" style="left:79px;top:3088px;width:230px;font-size:15px;line-height:26px;color:var(--white)">Lorem ipsum dolor sit amet, to consectetur adipiscing elit, sed do eiusmod tempor.</p>
<h4 class="abs" style="left:348px;top:3019px;font-family:'Montserrat',sans-serif;font-weight:700;font-size:20px;color:var(--white)">Quick Links</h4>
<span class="foot-link" style="left:348px;top:3071px">About Us</span>
<span class="foot-link" style="left:348px;top:3102px">Area Served</span>
<span class="foot-link" style="left:348px;top:3133px">Pricing &amp; Services</span>
<span class="foot-link" style="left:348px;top:3164px">Contact Us</span>
<span class="foot-link" style="left:617px;top:3071px">Terms &amp; Conditions</span>
<span class="foot-link" style="left:617px;top:3102px">Privacy &amp; Policy</span>
<span class="foot-link" style="left:617px;top:3133px">FAQS</span>
<span class="foot-link" style="left:617px;top:3164px">Help &amp; Support</span>
<p class="abs" style="left:885px;top:3100px;width:240px;font-size:15px;line-height:26px;color:var(--white)">123, Address, State Name, City Name, Zipcode</p>
<span class="foot-link" style="left:885px;top:3164px;font-weight:700;font-size:16px">123.456.789</span>
<span class="abs" style="left:884px;top:3008px;font-size:18px;color:var(--orange)">Follow On :</span>
<svg class="abs" style="left:1001px;top:3003px" width="122" height="36"><circle cx="18" cy="18" r="17" fill="#fff"/><circle cx="61" cy="18" r="17" fill="#fff"/><circle cx="104" cy="18" r="17" fill="#fff"/></svg>
<div class="abs" style="left:77px;top:3241px;width:1046px;height:1px;background:rgba(255,255,255,.35)"></div>
<p class="abs" style="left:0;width:1200px;text-align:center;top:3273px;font-size:15px;color:#fde3c2">© Copyright <b style="color:#fff">Brava Nest</b> - 2020 . All Right Reserved.</p>

</body>
</html>
```